Powerpoint template for Marlowe Stewardship Partners

I would like to use my logo and colors to create a powerpoint deck that I can use for various presentations. I would want the design to be modern, use my logo on each page (small at the bottom by the slide number) and have a couple of transition slides for cover page, transition page, etc.

```html
<!DOCTYPE html>
<html lang="en">
<head>
<meta charset="utf-8">
<title>Marlowe Stewardship Partners – Presentation Template</title>
<link href="https://fonts.googleapis.com/css2?family=Poppins:wght@300;400;500;600;700&display=swap" rel="stylesheet">
<style>
:root{
  --blue:#2458dc;
  --blue-soft:#dfe7fb;
  --grey:#5e5e5e;
  --grey-light:#e3e3e3;
  --ink:#4a4a4a;
  --bg:#c9cacc;
  --white:#fff;
}
*{margin:0;padding:0;box-sizing:border-box}
html,body{width:1200px;height:782px;overflow:hidden;background:var(--bg);font-family:'Poppins',sans-serif;color:var(--ink)}
.board{position:relative;width:1200px;height:782px}
.slide{position:absolute;width:206px;height:115px;background:var(--white);overflow:hidden;box-shadow:0 2px 6px rgba(0,0,0,.12)}
.c1{left:68px}.c2{left:283px}.c3{left:497px}.c4{left:711px}.c5{left:926px}
.r1{top:69px}.r2{top:201px}.r3{top:333px}.r4{top:465px}.r5{top:597px}
.abs{position:absolute}
.logo{position:absolute;top:8px;right:10px;font-size:5px;font-weight:600;color:var(--blue);letter-spacing:.3px;display:flex;align-items:center;gap:2px}
.logo::before{content:"";width:3px;height:3px;border-radius:50%;background:currentColor}
.logo.white{color:var(--white)}
.logo.left{left:11px;right:auto;top:12px;font-size:6.5px}
.foot{position:absolute;bottom:4px;left:11px;font-size:2.2px;color:var(--ink)}
.foot.white{color:var(--white)}
.num{position:absolute;bottom:4px;right:11px;font-size:2.2px}
.rule{position:absolute;bottom:9px;left:11px;right:11px;height:.3px;background:#bbb}
.photo{position:absolute}
.h-blue{font-size:4.6px;font-weight:600;color:var(--blue);text-transform:uppercase;text-decoration:underline;text-underline-offset:1px}
.p{font-size:3.3px;line-height:1.55}
.bul{font-size:3.3px;line-height:1;list-style:none}
.bul li{margin-top:4px}
.bul li::before{content:"•";margin-right:2px}
.tag{display:inline-block;border:.4px solid #999;font-size:2.6px;padding:1px 2px}
.cover-text{position:absolute;left:11px;top:41px;width:100px}
.title{font-size:6.4px;color:var(--blue);margin-top:2px;white-space:nowrap}
.sub{font-size:4.2px;line-height:1.35}
.ol{list-style:none;font-size:3.3px}
.ol li{display:flex;align-items:center;gap:3px;height:10px}
.dot{width:5px;height:5px;border-radius:50%;background:var(--blue);color:#fff;font-size:2.6px;display:flex;align-items:center;justify-content:center;flex:none}
.card{position:absolute;background:#fff;border:.5px solid #bbb;padding:8px 7px}
.card b{display:block;font-size:3.8px;color:var(--blue);font-weight:600;margin-bottom:3px}
.card .p{font-size:3px}
.white-t{color:#fff}
</style>
</head>
<body>
<div class="board">

<!-- Row 1 -->
<section class="slide c1 r1">
  <div class="photo" role="img" aria-label="Black and white mountain range" style="inset:0;background:linear-gradient(160deg,#e8e8e8,#8a8a8a 45%,#3a3a3a);clip-path:polygon(138px 0,206px 0,206px 115px,100px 115px)"></div>
  <div class="logo left">MARLOWE</div>
  <div class="cover-text">
    <span class="tag">Keynote Speaker</span>
    <div class="title">Marlowe Stewardship Partners</div>
    <div class="sub" style="width:90px">Helping leaders and organizations reach their next summit</div>
  </div>
  <div class="foot">www.marlowestewardship.com</div>
</section>

<section class="slide c2 r1" style="background:var(--blue)">
  <div class="logo left white">MARLOWE</div>
  <div class="cover-text white-t" style="top:43px;width:120px">
    <span class="tag" style="border-color:#fff">Keynote Speaker</span>
    <div class="title" style="color:#fff">Marlowe Stewardship Partners</div>
    <div class="sub" style="width:100px">Helping leaders and organizations reach their next summit</div>
  </div>
  <div class="foot white">www.marlowestewardship.com</div>
</section>

<section class="slide c3 r1">
  <div class="logo left">MARLOWE</div>
  <div class="cover-text" style="width:120px">
    <span class="tag">Keynote Speaker</span>
    <div class="title">Marlowe Stewardship Partners</div>
    <div class="sub" style="width:100px">Helping leaders and organizations reach their next summit</div>
  </div>
  <div class="foot">www.marlowestewardship.com</div>
</section>

<section class="slide c4 r1">
  <div class="abs" style="left:0;top:0;width:62px;height:115px;background:var(--blue)"></div>
  <div class="logo">MARLOWE</div>
  <div class="photo" role="img" aria-label="Portrait of the founder" style="left:35px;top:38px;width:42px;height:42px;background:linear-gradient(#e9e4de,#c9b9a6);border:1px solid #fff"></div>
  <div class="abs" style="left:90px;top:38px;width:104px">
    <div style="font-size:4.6px;font-weight:600;color:var(--blue)">About us</div>
    <p class="p" style="font-size:2.2px;margin-top:2px">Marlowe Stewardship Partners was founded to guide leaders through change. Our team brings decades of coaching, strategy and culture work to every client engagement.</p>
    <p class="p" style="font-size:2.2px;margin-top:2px">Our mission is to help leaders and teams build trust, align purpose and deliver lasting results.</p>
  </div>
  <div class="foot white">www.marlowestewardship.com</div>
  <div class="num">4</div>
</section>

<section class="slide c5 r1">
  <div class="photo" role="img" aria-label="Dark mountain peak" style="inset:0;background:linear-gradient(150deg,#5a5a5a,#747474 50%,#4e4e4e)"></div>
  <div class="logo white" style="font-size:6px;top:14px">MARLOWE</div>
  <div class="abs white-t" style="right:10px;top:52px;text-align:right">
    <div style="font-size:5px">SECTION 1</div>
    <div style="font-size:9px;line-height:1.1">Heading Goes Here</div>
  </div>
  <div class="foot white">www.marlowestewardship.com</div>
  <div class="num white-t">5</div>
</section>

<!-- Row 2 -->
<section class="slide c1 r2" style="background:var(--blue)">
  <div class="photo" role="img" aria-label="Circle of dominoes with a single red one" style="left:0;top:0;width:113px;height:115px;background:radial-gradient(circle at 55% 45%,#c33 0 5%,#222 18%,#9a9a9a 45%,#3a3a3a 80%)"></div>
  <div class="logo white" style="top:11px;right:10px;font-size:6.5px">MARLOWE</div>
  <div class="abs white-t" style="left:123px;top:51px">
    <div style="font-size:3.2px">SECTION 1</div>
    <div style="font-size:7.5px;line-height:1.2">Heading<br>Goes Here</div>
  </div>
  <div class="rule" style="left:123px;background:#7e9ff0"></div>
  <div class="foot white">www.marlowestewardship.com</div>
  <div class="num white-t">6</div>
</section>

<section class="slide c2 r2">
  <div class="abs" style="inset:0;background:var(--grey);clip-path:polygon(0 0,67px 0,82px 115px,0 115px)"></div>
  <div class="logo">MARLOWE</div>
  <div class="abs white-t" style="left:20px;top:44px;font-size:4.6px;font-weight:600">AGENDA</div>
  <ul class="ol abs" style="left:68px;top:30px">
    <li><span class="dot">1</span>Increase the impact of your presentations</li>
    <li style="margin-left:1px"><span class="dot">2</span>Polish delivery skills to enhance audience engagement</li>
    <li style="margin-left:2px"><span class="dot">3</span>Apply storytelling techniques to contextualize data</li>
    <li style="margin-left:4px"><span class="dot">4</span>Encourage and manage audience participation</li>
    <li style="margin-left:5px"><span class="dot">5</span>Exhibit confidence and composure during Q&amp;A</li>
  </ul>
  <div class="rule" style="left:82px"></div>
  <div class="foot white">www.marlowestewardship.com</div>
  <div class="num">7</div>
</section>

<section class="slide c3 r2">
  <div class="abs" style="left:126px;top:0;width:80px;height:115px;background:var(--blue)"></div>
  <div class="logo white">MARLOWE</div>
  <div class="abs" style="left:12px;top:20px;width:108px">
    <div class="h-blue" style="text-decoration:none">WELCOME &amp; OPENING REMARKS</div>
    <p class="p" style="margin-top:7px">Lorem Ipsum is simply dummy text of the printing and typesetting industry. Lorem Ipsum has been the industry's standard dummy text ever since the 1500.</p>
    <ul class="bul"><li>It has survived not only five centuries.</li><li>It was popularised in the 1960s.</li><li>Lorem Ipsum passages, and mor.</li><li>recently with desktop publishing software.</li></ul>
  </div>
  <p class="abs p white-t" style="left:144px;top:43px;width:42px">Lorem Ipsum has been the industry's standard dummy text ever since the 1500.</p>
  <div class="rule"></div>
  <div class="foot">www.marlowestewardship.com</div>
  <div class="num white-t">8</div>
</section>

<section class="slide c4 r2">
  <div class="abs" style="left:0;right:0;top:67px;bottom:0;background:var(--grey)"></div>
  <div class="logo">MARLOWE</div>
  <div class="h-blue abs" style="left:0;right:0;top:20px;text-align:center">OUR PHILOSOPHY (MIND + BODY)</div>
  <div class="card" style="left:23px;top:39px;width:77px;height:62px"><b>Corporate — Mind</b><p class="p">Lorem Ipsum is simply dummy text of the printing and typesetting industry. Lorem Ipsum has been the industry's standard dummy text ever since the 1500.</p></div>
  <div class="card" style="left:106px;top:39px;width:77px;height:62px"><b>Movement — Body</b><p class="p">Lorem Ipsum is simply dummy text of the printing and typesetting industry. Lorem Ipsum has been the industry's standard dummy text ever since the 1500.</p></div>
  <div class="rule" style="background:#999"></div>
  <div class="foot white">www.marlowestewardship.com</div>
  <div class="num white-t">9</div>
</section>

<section class="slide c5 r2">
  <div class="abs" style="left:0;right:0;top:0;height:57px;background:var(--blue)"></div>
  <div class="logo white">MARLOWE</div>
  <div class="h-blue abs" style="left:12px;top:19px;color:#fff">HEADING GOES HERE</div>
  <div class="card" style="left:11px;top:39px;width:58px;height:62px;border-color:var(--blue);padding:8px 3px"><b>Sub Heading</b><p class="p">Lorem Ipsum is simply dummy text of the printing and typesetting industry. Lorem Ipsum has been the industry's standard dummy text ever since the 1500.</p></div>
  <div class="card" style="left:75px;top:39px;width:58px;height:62px;border-color:var(--blue);padding:8px 3px"><b>Sub Heading</b><p class="p">Lorem Ipsum is simply dummy text of the printing and typesetting industry. Lorem Ipsum has been the industry's standard dummy text ever since the 1500.</p></div>
  <div class="card" style="left:137px;top:39px;width:58px;height:62px;border-color:var(--blue);padding:8px 3px"><b>Sub Heading</b><p class="p">Lorem Ipsum is simply dummy text of the printing and typesetting industry. Lorem Ipsum has been the industry's standard dummy text ever since the 1500.</p></div>
  <div class="rule"></div>
  <div class="foot">www.marlowestewardship.com</div>
  <div class="num">10</div>
</section>

<!-- Row 3 -->
<section class="slide c1 r3">
  <div class="abs" style="left:0;top:0;width:82px;height:115px;background:var(--blue)"></div>
  <div class="abs white-t" style="left:17px;top:36px;width:58px">
    <div style="font-size:4.6px;font-weight:600">WHAT WE DO</div>
    <p class="p" style="margin-top:2px">Lorem Ipsum is simply dummy text of the printing and typesetting industry. Lorem Ipsum has been the industry's standard dummy text ever since the 1500.</p>
  </div>
  <div class="logo">MARLOWE</div>
  <div class="abs" style="left:98px;top:27px;font-size:4.4px;font-weight:600">WE DESIGN AND DELIVER</div>
  <svg class="abs" style="left:98px;top:36px" width="94" height="60" viewBox="0 0 94 60" font-family="Poppins,sans-serif" font-size="2.6" fill="#2458dc" text-anchor="middle">
    <g fill="none" stroke="#8a8a8a" stroke-width=".4">
      <rect x=".2" y=".2" width="28" height="27"/><rect x="32" y=".2" width="28" height="27"/><rect x="63.8" y=".2" width="28" height="27"/>
      <rect x=".2" y="30.5" width="28" height="27"/><rect x="32" y="30.5" width="28" height="27"/><rect x="63.8" y="30.5" width="28" height="27"/>
    </g>
    <g fill="none" stroke="#2458dc" stroke-width=".5">
      <circle cx="14.2" cy="9" r="4"/><circle cx="46" cy="9" r="4"/><circle cx="77.8" cy="9" r="4"/>
      <circle cx="14.2" cy="39.5" r="4"/><circle cx="46" cy="39.5" r="4"/><circle cx="77.8" cy="39.5" r="4"/>
    </g>
    <text x="14.2" y="19">Executive</text><text x="14.2" y="22.5">Coaching</text>
    <text x="46" y="19">Leadership</text><text x="46" y="22.5">Programs</text>
    <text x="77.8" y="19">Team</text><text x="77.8" y="22.5">Workshops</text>
    <text x="14.2" y="49.5">Culture &amp; Trust</text><text x="14.2" y="53">Building</text>
    <text x="46" y="49.5">Strategy</text><text x="46" y="53">Offsites</text>
    <text x="77.8" y="49.5">Psychometric</text><text x="77.8" y="53">Tools</text>
  </svg>
  <div class="rule" style="left:82px"></div>
  <div class="foot white">www.marlowestewardship.com</div>
  <div class="num">11</div>
</section>

<section class="slide c2 r3">
  <div class="abs" style="inset:0;background:var(--grey);clip-path:polygon(137px 0,206px 0,206px 115px,122px 115px)"></div>
  <div class="logo white">MARLOWE</div>
  <div class="abs" style="left:12px;top:27px;width:84px">
    <div class="h-blue">HEADING GOES HERE</div>
    <p class="p" style="margin-top:4px">Lorem Ipsum is simply dummy text of the printing and typesetting industry. Lorem Ipsum has been the industry's standard dummy text ever since the 1500.</p>
    <p class="p" style="margin-top:3px">Lorem Ipsum is simply dummy text of the printing and typesetting industry. Lorem Ipsum has been the industry's standard dummy text ever since the 1500.</p>
  </div>
  <div class="photo" role="img" aria-label="Team meeting in a bright office" style="left:108px;top:32px;width:88px;height:63px;background:linear-gradient(120deg,#cfd6dc,#8c949c 55%,#e7e2dc)"></div>
  <div class="rule"></div>
  <div class="foot">www.marlowestewardship.com</div>
  <div class="num white-t">12</div>
</section>

<section class="slide c3 r3">
  <div class="photo" role="img" aria-label="Two colleagues reviewing a document together" style="left:0;top:0;width:90px;height:115px;background:linear-gradient(135deg,#4f6f86,#9aa6ae 45%,#2f3f55)"></div>
  <div class="logo">MARLOWE</div>
  <div class="abs" style="left:108px;top:44px;font-size:4.6px;font-weight:600;color:var(--blue);line-height:1.2">
    <div>Increase the impact<br>of your presentations</div>
    <div style="margin-top:4px">Increase the impact<br>of your presentations</div>
  </div>
  <div class="rule" style="left:90px"></div>
  <div class="foot white">www.marlowestewardship.com</div>
  <div class="num">13</div>
</section>

<section class="slide c4 r3">
  <div class="logo">MARLOWE</div>
  <div class="abs" style="left:12px;top:16px;width:185px">
    <div class="h-blue" style="text-decoration:none">HEADING GOES HERE</div>
    <div style="font-size:4.2px;font-weight:500;margin-top:10px">Sub Heading</div>
    <p class="p" style="margin-top:3px">Lorem Ipsum is simply dummy text of the printing and typesetting industry.<br>Lorem Ipsum has been the industry's standard dummy text ever since the 1500.</p>
    <ul class="bul" style="margin-left:1px"><li>It has survived not only five centuries.</li><li>It was popularised in the 1960s.</li><li>Lorem Ipsum passages, and mor.</li><li>recently with desktop publishing software.</li></ul>
  </div>
  <div class="rule"></div>
  <div class="foot">www.marlowestewardship.com</div>
  <div class="num">14</div>
</section>

<section class="slide c5 r3">
  <div class="logo">MARLOWE</div>
  <div class="h-blue abs" style="left:17px;top:19px">OUR APPROACH</div>
  <div class="abs" style="left:17px;top:36px;width:54px;height:64px;background:var(--grey-light);padding:5px 4px">
    <div style="font-size:3.8px;font-weight:500;line-height:1.1">RELATIONSHIP MANAGEMENT</div>
    <p class="p" style="font-size:3px;margin-top:2px">Lorem Ipsum is simply dummy text of the printing and typesetting industry. Lorem Ipsum has been the industry's standard dummy text ever since the 1500.</p>
  </div>
  <div class="abs" style="left:74px;top:36px;width:54px;height:64px;background:var(--grey-light);padding:5px 4px">
    <div style="font-size:3.8px;font-weight:500;line-height:1.1">LEADERSHIP COACHING</div>
    <p class="p" style="font-size:3px;margin-top:2px">Lorem Ipsum is simply dummy text of the printing and typesetting industry. Lorem Ipsum has been the industry's standard dummy text ever since the 1500.</p>
  </div>
  <div class="abs white-t" style="left:131px;top:36px;width:55px;height:64px;background:var(--blue);padding:5px 4px">
    <div style="font-size:3.8px;font-weight:600;line-height:1.1">GROWTH STARTEGIES</div>
    <p class="p" style="font-size:3px;margin-top:2px">Lorem Ipsum is simply dummy text of the printing and typesetting industry. Lorem Ipsum has been the industry's standard dummy text ever since the 1500.</p>
  </div>
  <div class="rule"></div>
  <div class="foot">www.marlowestewardship.com</div>
  <div class="num">15</div>
</section>

<!-- Row 4 -->
<section class="slide c1 r4">
  <div class="abs" style="left:0;right:0;top:0;height:25px;background:var(--blue)"></div>
  <div class="abs white-t" style="left:11px;top:10px;font-size:4.6px;font-weight:600">TODAY'S AGENDA</div>
  <div class="logo white" style="top:11px">MARLOWE</div>
  <table class="abs" style="left:11px;top:32px;width:184px;border-collapse:collapse;font-size:2.8px">
    <thead><tr style="background:var(--grey);color:#fff;text-align:left"><th style="padding:.8px 1px">DATE</th><th>TIME</th><th>TOPIC</th></tr></thead>
    <tbody>
      <tr><td style="padding:2.2px 1px">21-11-2025</td><td>09:00</td><td>WELCOME &amp; OPENING REMARKS</td></tr>
      <tr><td style="padding:2.2px 1px">21-11-2025</td><td>09:00</td><td>LEADERSHIP: WHAT DOES GREAT LOOK LIKE?</td></tr>
      <tr><td style="padding:2.2px 1px">21-11-2025</td><td>09:00</td><td>STRENGTHENING CULTURE GLOBALLY</td></tr>
      <tr><td style="padding:2.2px 1px">21-11-2025</td><td>09:00</td><td>LUNCH</td></tr>
      <tr><td style="padding:2.2px 1px">21-11-2025</td><td>09:00</td><td>STRATEGIC DIALOGUE: FUTURE &amp; PRIORITIES</td></tr>
      <tr><td style="padding:2.2px 1px">21-11-2025</td><td>09:00</td><td>ACTION PLANNING</td></tr>
      <tr><td style="padding:2.2px 1px">21-11-2025</td><td>09:00</td><td>CLOSING REMARKS</td></tr>
    </tbody>
  </table>
  <svg class="abs" style="left:11px;top:37px" width="184" height="64"><g stroke="#aaa" stroke-width=".3"><line x1="0" x2="184" y1="8.7" y2="8.7"/><line x1="0" x2="184" y1="17.7" y2="17.7"/><line x1="0" x2="184" y1="26.6" y2="26.6"/><line x1="0" x2="184" y1="35.5" y2="35.5"/><line x1="0" x2="184" y1="44.5" y2="44.5"/><line x1="0" x2="184" y1="53.4" y2="53.4"/><line x1="0" x2="184" y1="62.3" y2="62.3"/></g></svg>
  <div class="rule"></div>
  <div class="foot">www.marlowestewardship.com</div>
  <div class="num">16</div>
</section>

<section class="slide c2 r4">
  <div class="abs" style="left:0;top:0;width:130px;height:115px;background:var(--blue)"></div>
  <div class="logo">MARLOWE</div>
  <div class="abs white-t" style="left:24px;top:46px;font-size:10px;font-weight:600;line-height:1.1">COFFEE<br>BREAK</div>
  <div class="abs" style="left:85px;top:15px;width:87px;height:87px;border-radius:50%;background:#fff;box-shadow:0 1px 3px rgba(0,0,0,.2)"></div>
  <div class="photo" role="img" aria-label="Cup of latte with foam art" style="left:89px;top:19px;width:79px;height:79px;border-radius:50%;background:radial-gradient(circle at 45% 55%,#f4ead9 0 14%,#b4763e 22%,#6e3f1e 55%,#3a2618)"></div>
  <div class="rule" style="background:#7e9ff0"></div>
  <div class="foot white">www.marlowestewardship.com</div>
  <div class="num">17</div>
</section>

<section class="slide c3 r4">
  <div class="logo">MARLOWE</div>
  <div class="h-blue abs" style="left:12px;top:22px">GROUP ACTIVITY SLIDE</div>
  <ul class="ol abs" style="left:12px;top:41px;width:99px;font-size:3px">
    <li style="border-bottom:.3px solid #aaa"><span class="dot" style="background:var(--grey)">1</span>Discuss what each value means to you</li>
    <li style="border-bottom:.3px solid #aaa"><span class="dot" style="background:var(--grey)">2</span>Identify behaviors that reinforce the value</li>
    <li style="border-bottom:.3px solid #aaa"><span class="dot" style="background:var(--grey)">3</span>Capture shared statements on whiteboard/flipchart</li>
    <li style="border-bottom:.3px solid #aaa"><span class="dot" style="background:var(--grey)">4</span>Discuss what each value means to you</li>
    <li style="border-bottom:.3px solid #aaa"><span class="dot" style="background:var(--grey)">5</span>Identify behaviors that reinforce the value</li>
  </ul>
  <div class="abs white-t" style="left:119px;top:42px;width:87px;height:49px;background:var(--blue);padding:7px 9px">
    <p class="p">Lorem Ipsum is simply dummy text of the printing and typesetting industry. Lorem Ipsum has been the industry's standard dummy text ever since the 1500.</p>
  </div>
  <div class="rule"></div>
  <div class="foot">www.marlowestewardship.com</div>
  <div class="num">18</div>
</section>

<section class="slide c4 r4">
  <div class="logo">MARLOWE</div>
  <div class="abs" style="left:37px;top:26px;width:133px;height:54px;border:.8px solid var(--grey);border-radius:3px;text-align:center;color:var(--blue);padding:10px 22px">
    <div style="font-size:7px;font-weight:700;line-height:.6">“</div>
    <p class="p" style="font-size:3.5px">Lorem Ipsum is simply dummy text of the printing and typesetting industry. Lorem Ipsum has been the industry's standard dummy text ever since the 1500.</p>
    <div style="font-size:7px;font-weight:700;line-height:1">“</div>
  </div>
  <div class="rule"></div>
  <div class="foot">www.marlowestewardship.com</div>
  <div class="num">19</div>
</section>

<section class="slide c5 r4" style="background:var(--blue)">
  <div class="abs" style="left:11px;top:10px;width:185px;height:95px;background:#fff"></div>
  <div class="logo" style="top:20px;right:17px;font-size:4.4px">MARLOWE</div>
  <div class="h-blue abs" style="left:0;right:0;top:21px;text-align:center">BREAKOUT INSTRUCTIONS</div>
  <svg class="abs" style="left:11px;top:30px" width="185" height="65" viewBox="0 0 185 65" font-family="Poppins,sans-serif" font-size="3.3" text-anchor="middle">
    <g fill="none" stroke="#2458dc" stroke-width="1.2">
      <path d="M12 22 A15 15 0 0 0 42 22"/>
      <path d="M47 24 A15 15 0 0 1 77 24" stroke="#5e5e5e"/>
      <path d="M79 24 A15 15 0 0 0 109 24"/>
      <path d="M111 24 A15 15 0 0 1 141 24" stroke="#5e5e5e"/>
      <path d="M142 22 A15 15 0 0 0 172 22"/>
    </g>
    <g fill="#2458dc"><circle cx="27" cy="37" r="3.5"/><circle cx="94" cy="39" r="3.5"/><circle cx="157" cy="37" r="3.5"/></g>
    <g fill="#5e5e5e"><circle cx="62" cy="9" r="3.5"/><circle cx="126" cy="9" r="3.5"/></g>
    <g fill="#fff" font-size="2.8"><text x="27" y="38">01</text><text x="62" y="10">02</text><text x="94" y="40">03</text><text x="126" y="10">04</text><text x="157" y="38">05</text></g>
    <g fill="#4a4a4a"><text x="27" y="51">Lorem Ipsum is</text><text x="27" y="55">simply dummy?</text>
    <text x="62" y="19">Lorem</text><text x="62" y="23">Ipsum is</text><text x="62" y="27">simply</text><text x="62" y="31">dummy?</text>
    <text x="94" y="51">Lorem Ipsum is</text><text x="94" y="55">simply dummy?</text>
    <text x="126" y="19">Lorem</text><text x="126" y="23">Ipsum is</text><text x="126" y="27">simply</text><text x="126" y="31">dummy?</text>
    <text x="157" y="51">Lorem Ipsum is</text><text x="157" y="55">simply dummy?</text></g>
  </svg>
  <div class="foot white">www.marlowestewardship.com</div>
</section>

<!-- Row 5 -->
<section class="slide c1 r5">
  <div class="photo" role="img" aria-label="Colleagues laughing around a table" style="inset:0;background:linear-gradient(120deg,#cdbfae,#8c7c6a 45%,#e3ddd4 80%)"></div>
  <div class="logo white">MARLOWE</div>
</section>

<section class="slide c2 r5">
  <div class="logo">MARLOWE</div>
  <div class="h-blue abs" style="left:12px;top:23px">KEY TAKEAWAYS</div>
  <ul class="ol abs" style="left:12px;top:37px;width:118px">
    <li><span class="dot">1</span>Increase the impact of your presentations</li>
    <li><span class="dot">2</span>Polish delivery skills to enhance audience engagement</li>
    <li><span class="dot">3</span>Apply storytelling techniques to contextualize data</li>
    <li><span class="dot">4</span>Encourage and manage audience participation</li>
    <li><span class="dot">5</span>Exhibit confidence and composure during Q&amp;A</li>
  </ul>
  <div class="abs" style="left:135px;top:34px;width:60px;height:58px;background:var(--grey)"></div>
  <div class="rule"></div>
  <div class="foot">www.marlowestewardship.com</div>
  <div class="num">22</div>
</section>

<section class="slide c3 r5">
  <div class="logo">MARLOWE</div>
  <div class="abs" style="left:12px;top:16px;width:185px">
    <div class="h-blue" style="text-decoration:none">GROUP ACTIVITY SLIDE</div>
    <div style="font-size:4.2px;font-weight:500;margin-top:10px">Sub Heading</div>
    <p class="p" style="margin-top:3px">Lorem Ipsum is simply dummy text of the printing and typesetting industry.<br>Lorem Ipsum has been the industry's standard dummy text ever since the 1500.</p>
    <ul class="bul"><li>It has survived not only five centuries.</li><li>It was popularised in the 1960s.</li><li>Lorem Ipsum passages, and mor.</li><li>recently with desktop publishing software.</li></ul>
  </div>
  <div class="rule"></div>
  <div class="foot">www.marlowestewardship.com</div>
  <div class="num">21</div>
</section>

<section class="slide c4 r5">
  <div class="abs" style="left:127px;top:0;width:79px;height:115px;background:var(--grey)"></div>
  <div class="logo white">MARLOWE</div>
  <div class="h-blue abs" style="left:12px;top:19px;text-decoration:none">ACTION PLANNING</div>
  <div class="abs" style="left:12px;top:32px;width:110px">
    <div style="display:flex;gap:3px;height:16px"><span class="dot" style="margin-top:1px">1</span><div><div style="font-size:3.8px;font-weight:500">Lorem Ipsum is simply dummy?</div><div style="font-size:3px">Text of the printing and typesetting industry.</div></div></div>
    <div style="display:flex;gap:3px;height:16px"><span class="dot" style="margin-top:1px">1</span><div><div style="font-size:3.8px;font-weight:500">Lorem Ipsum is simply dummy?</div><div style="font-size:3px">Text of the printing and typesetting industry.</div></div></div>
    <div style="display:flex;gap:3px;height:16px"><span class="dot" style="margin-top:1px">1</span><div><div style="font-size:3.8px;font-weight:500">Lorem Ipsum is simply dummy?</div><div style="font-size:3px">Text of the printing and typesetting industry.</div></div></div>
    <div style="display:flex;gap:3px;height:16px"><span class="dot" style="margin-top:1px">1</span><div><div style="font-size:3.8px;font-weight:500">Lorem Ipsum is simply dummy?</div><div style="font-size:3px">Text of the printing and typesetting industry.</div></div></div>
  </div>
  <svg class="abs" style="left:137px;top:38px" width="54" height="40" viewBox="0 0 54 40" font-family="Poppins,sans-serif" font-weight="600" text-anchor="middle">
    <circle cx="17" cy="19" r="16" fill="#fff"/>
    <circle cx="39" cy="23" r="12" fill="#2458dc" stroke="#fff" stroke-width="1"/>
    <text x="17" y="27" font-size="22" fill="#2458dc">Q</text>
    <text x="39" y="30" font-size="17" fill="#fff">A</text>
  </svg>
  <div class="rule"></div>
  <div class="foot">www.marlowestewardship.com</div>
  <div class="num white-t">24</div>
</section>

<section class="slide c5 r5" style="background:var(--blue)">
  <div class="abs white-t" style="left:0;right:0;top:20px;text-align:center;font-size:7px;font-weight:600">MARLOWE</div>
  <div class="abs white-t" style="left:0;right:0;top:51px;text-align:center;font-size:10px;font-weight:600;letter-spacing:3px">THANK YOU</div>
  <div class="abs white-t" style="left:0;right:0;bottom:9px;text-align:center;font-size:2.2px">www.marlowestewardship.com</div>
</section>

</div>
</body>
</html>
```